Breezy Lanterns Handcrafted Copper Jewelry

I make handcrafted copper bracelets and cuffs.
I need a banner made (2' 1/2" x 10')
I attached the logo (I would like that sketch to be purple)
Company name: Breezy Lanterns (in a "sassy" font)
Tag line: Bring the Breeze
Designer/Creator: Marla Dunsby
481.307.6624
FB: www.facebook.com/breezylanterns.net
shop.breezylanterns.net
I'd like the background to be white. I'm not sure what I'm looking for as far as the look or if I should add any pics of the copper jewelry that I make. I'm totally up for suggestions. I'm very eager to see how creative you can be.
Many thanks.

```html
<!DOCTYPE html>
<html lang="en">
<head>
<meta charset="utf-8">
<title>Breezy Lanterns – Banner Options</title>
<link href="https://fonts.googleapis.com/css2?family=Berkshire+Swash&display=swap" rel="stylesheet">
<style>
  :root {
    --purple: #6a3d9e;
    --purple-light: #8a63b8;
    --purple-pale: #b59ad6;
    --white: #ffffff;
    --page: #ffffff;
  }
  * { margin: 0; padding: 0; box-sizing: border-box; }
  html, body { width: 900px; height: 1200px; overflow: hidden; background: var(--page); }
  body { position: relative; font-family: "Berkshire Swash", cursive; color: var(--white); }

  .banner {
    position: absolute; left: 69px; width: 762px; height: 200px;
    background: var(--purple);
  }
  .banner--one   { top: 84px; }
  .banner--two   { top: 372px; }
  .banner--three { top: 648px; }
  .banner--four  { top: 930px; }

  .figure-sketch {
    position: absolute; left: 18px; top: 12px; width: 80px; height: 176px;
    background: linear-gradient(180deg, var(--purple-pale), var(--purple-light));
    border-radius: 40px 40px 8px 8px; opacity: .55;
  }

  .credit { position: absolute; left: 112px; top: 18px; font-size: 17px; font-weight: 400; white-space: nowrap; }
  .brand-name {
    position: absolute; left: 112px; top: 74px;
    font-size: 38px; font-weight: 400; line-height: 1; white-space: nowrap;
  }

  .ribbon {
    position: absolute; background: var(--white); color: var(--purple);
    text-align: center; line-height: 1.05;
  }
  .ribbon--flag {
    left: 430px; top: 40px; width: 84px; padding: 8px 6px 22px;
    font-size: 19px;
    clip-path: polygon(0 0, 100% 0, 100% 100%, 50% 84%, 0 100%);
  }
  .ribbon--tag {
    left: 430px; top: 30px; width: 310px; padding: 4px 0;
    font-size: 28px;
    clip-path: polygon(0 0, 100% 0, 96% 50%, 100% 100%, 0 100%, 4% 50%);
  }
  .banner--four .ribbon--tag {
    background: none; color: var(--white); clip-path: none;
    border-bottom: 3px solid var(--white);
  }

  .contact { position: absolute; text-align: center; line-height: 1.2; white-space: nowrap; }
  .banner--one .contact { left: 530px; top: 34px; width: 220px; font-size: 16px; }
  .banner--one .contact .phone { font-size: 18px; }
  .contact--wide { left: 430px; top: 78px; width: 310px; font-size: 19px; }
  .contact--wide .phone { font-size: 40px; line-height: 1.05; }
  .banner--three .ribbon--flag { left: 560px; top: 10px; width: 80px; font-size: 17px; }
  .banner--three .contact { left: 450px; top: 98px; width: 300px; font-size: 19px; }
  .banner--three .contact .phone { font-size: 22px; }
  .contact .small { font-size: 12px; opacity: .8; }
</style>
</head>
<body>

<section class="banner banner--one">
  <div class="figure-sketch" role="img" aria-label="Purple sketch of a woman, the Breezy Lanterns figure"></div>
  <p class="credit">Designer/Creator - Marla Dunsby</p>
  <h1 class="brand-name">Breezy Lanterns</h1>
  <div class="ribbon ribbon--flag">Bring the Breeze</div>
  <div class="contact">
    <p class="small">Bracelets</p>
    <p>shop.breezylanterns.net</p>
    <p class="phone">481.307.6624</p>
    <p>breezylanterns.net</p>
    <p class="small">facebook</p>
  </div>
</section>

<section class="banner banner--two">
  <div class="figure-sketch" role="img" aria-label="Purple sketch of a woman, the Breezy Lanterns figure"></div>
  <p class="credit">Designer/Creator - Marla Dunsby</p>
  <h2 class="brand-name">Breezy Lanterns</h2>
  <div class="ribbon ribbon--tag">Bring the Breeze</div>
  <div class="contact contact--wide">
    <p>www.shop.breezylanterns.net</p>
    <p class="phone">481.307.6624</p>
    <p>facebook/breezylanterns.net</p>
  </div>
</section>

<section class="banner banner--three">
  <div class="figure-sketch" role="img" aria-label="Purple sketch of a woman, the Breezy Lanterns figure"></div>
  <p class="credit">Designer/Creator - Marla Dunsby</p>
  <h2 class="brand-name">Breezy Lanterns</h2>
  <div class="ribbon ribbon--flag">Bring the Breeze</div>
  <div class="contact">
    <p class="phone">481.307.6624</p>
    <p>facebook/breezylanterns.net</p>
    <p>www.shop.breezylanterns.net</p>
  </div>
</section>

<section class="banner banner--four">
  <div class="figure-sketch" role="img" aria-label="Purple sketch of a woman, the Breezy Lanterns figure"></div>
  <p class="credit">Designer/Creator - Marla Dunsby</p>
  <h2 class="brand-name">Breezy Lanterns</h2>
  <div class="ribbon ribbon--tag">Bring the Breeze</div>
  <div class="contact contact--wide">
    <p>www.shop.breezylanterns.net</p>
    <p class="phone">481.307.6624</p>
    <p>facebook/breezylanterns.net</p>
  </div>
</section>

</body>
</html>
```